Website Design for Camp 3874

We need a website design for a new company that strives to provide training and structure for religious missionaries who are traveling the world to teach of christianity.
They provide training in:
- Nutrition Coaching & Daily assignments
- Personal Training Sessions
- Phycological emotional/mental component
The goal of Camp 3874 is to help missionaries preach the gospel of christ to those who haven't heard it due to geographical obstacles and physical limitations that get in the way.
The homepage template has linked images to use. If any other images are needed, stock images are acceptable.

Logo/Color Scheme: https://files.nervalo.example/folders/8Kp2QwZr7LmXv4TsN9bHc3YdJ6fGaE1Ru?share=open

Customer Avatar/Core Message Canvas: https://sheets.nervalo.example/s/d/7Hq39TbWmuKpZr2LxNcV8yEs5DfGa4JkQo1BnXtYRMwP/edit?share=open

Homepage Template: https://pages.nervalo.example/doc/d/5nRZ82kLp94QsWxTy7mBuVhCe3DjFa6Go0PiKqNr4Ytw/edit?share=open

```html
<!DOCTYPE html>
<html lang="en">
<head>
<meta charset="utf-8">
<title>Camp 3874 — Mind + Body + Spirit</title>
<link rel="stylesheet" href="https://fonts.googleapis.com/css2?family=Montserrat:wght@600;700;800;900&family=Outfit:wght@300;400;500;600&display=swap">
<style>
:root{
  --forest:#2b3a1b;
  --olive:#5b6b2f;
  --gold:#e2b845;
  --cream:#fdf7e6;
  --mist:#f3f3f3;
  --ink:#1d1d1d;
  --text:#444;
  --white:#fff;
}
*{box-sizing:border-box;margin:0;padding:0}
html,body{width:1200px;height:4937px;overflow:hidden;background:var(--white)}
body{position:relative;font-family:"Outfit",sans-serif;color:var(--text)}
.abs{position:absolute}
h1,h2,h3,.heading{font-family:"Montserrat",sans-serif;color:var(--ink);font-weight:800}
.btn{position:absolute;display:flex;align-items:center;justify-content:center;font-family:"Outfit",sans-serif;font-size:13px;font-weight:600}
.btn-olive{background:var(--olive);color:var(--white)}
.btn-gold{background:var(--gold);color:var(--forest)}
.btn-outline{border:2px solid var(--olive);color:var(--olive);background:var(--white)}
.photo{position:absolute}

/* header */
.header-rule{position:absolute;top:52px;height:1px;background:#cfcfcf}
.brand{position:absolute;left:480px;top:22px;width:240px;text-align:center}
.brand-name{font-family:"Montserrat",sans-serif;font-weight:900;font-size:36px;color:var(--forest);letter-spacing:1px;line-height:40px}
.brand-tag{font-family:"Montserrat",sans-serif;font-weight:700;font-size:10px;letter-spacing:4px;color:var(--forest)}

/* hero */
.hero{left:34px;top:107px;width:1132px;height:666px;background:linear-gradient(180deg,#6c7c86 0%,#8a8c88 30%,#4b3f30 65%,#2a241b 100%)}
.nav{position:absolute;left:159px;top:128px;width:882px;height:50px;background:var(--white);display:flex;align-items:center;justify-content:space-around;font-size:11px;color:var(--ink)}
.nav span{flex:1;text-align:center;border-right:1px solid var(--gold);line-height:14px}
.nav span:last-child{border-right:0}
.hero-title{position:absolute;left:0;width:1200px;top:450px;text-align:center;color:var(--white);font-size:54px;font-weight:900;font-family:"Montserrat",sans-serif}
.hero-sub{position:absolute;left:0;width:1200px;top:512px;text-align:center;color:var(--white);font-family:"Montserrat",sans-serif;font-weight:700;font-size:30px;line-height:37px}
.hero-copy{position:absolute;left:330px;width:540px;top:607px;text-align:center;color:var(--white);font-size:13px;line-height:19px}

/* sections */
.section-title{position:absolute;left:125px;font-size:35px;line-height:44px;font-weight:800}
.cream{background:var(--cream)}
.para{font-size:13px;line-height:19px;color:var(--text)}
.tab{position:absolute;top:2400px;width:222px;height:50px;display:flex;align-items:center;justify-content:center;font-weight:600;font-size:16px;border:1px solid #777;color:var(--ink)}
.tab.is-active{background:var(--forest);color:var(--white);border-color:var(--forest)}
.card-title{position:absolute;top:3582px;width:303px;font-family:"Montserrat",sans-serif;font-weight:800;font-size:20px;line-height:25px;color:var(--ink)}
.card-copy{position:absolute;width:303px;font-size:13px;line-height:19px}

/* footer */
.footer{left:23px;top:4392px;width:1131px;height:477px;background:var(--forest)}
.foot-head{position:absolute;top:4484px;font-family:"Montserrat",sans-serif;font-weight:800;font-size:24px;color:var(--white)}
.foot-link{position:absolute;left:477px;font-size:13px;color:var(--white)}
.contact{position:absolute;left:771px;display:flex;align-items:center;gap:16px;color:var(--white);font-size:15px;line-height:21px}
.contact-icon{width:46px;height:46px;border-radius:50%;background:var(--gold);display:flex;align-items:center;justify-content:center;flex:none}
.social{position:absolute;top:4694px;width:16px;height:16px;border-radius:50%;background:var(--white)}
.legal{position:absolute;top:4897px;font-size:12px;color:#555}
</style>
</head>
<body>

<!-- Header -->
<div class="header-rule" style="left:34px;width:420px"></div>
<div class="header-rule" style="left:746px;width:420px"></div>
<div class="brand">
  <div class="brand-name">CAMP 3874</div>
  <div class="brand-tag">MIND + BODY + SPIRIT</div>
</div>

<!-- Hero -->
<div class="abs hero" role="img" aria-label="Person with a backpack sitting on a ridge facing snowy mountains at dusk"></div>
<nav class="nav"><span>Programs</span><span>Events</span><span>Online Store</span><span>About Us</span><span>Contact Us</span></nav>
<h1 class="hero-title">EMPOWING CHANGE</h1>
<div class="hero-sub">By Illuminating Lives Unexposed to The<br>Gospel’s Light</div>
<p class="hero-copy">Camp 3874’s mission is to enable the word of Jesus to be experienced by people in the most remote and treacherous parts of the world</p>
<div class="btn" style="left:406px;top:675px;width:186px;height:42px;border:1px solid var(--olive);color:var(--white);background:rgba(0,0,0,.25)">View Our Programs</div>
<div class="btn btn-olive" style="left:606px;top:675px;width:186px;height:42px">Register for Training</div>
<svg class="abs" style="left:1062px;top:723px" width="80" height="90" viewBox="0 0 80 90">
  <polygon points="40,2 78,23 78,67 40,88 2,67 2,23" fill="var(--gold)"/>
  <circle cx="40" cy="36" r="10" fill="var(--forest)"/>
  <path d="M22 62c0-11 8-16 18-16s18 5 18 16z" fill="var(--forest)"/>
</svg>

<!-- Staff -->
<h2 class="section-title" style="top:866px">CAMP 3874’S WELL-ROUNDED<br>STAFF FOR SPECIALIZED TRAINING</h2>
<div class="photo" style="left:125px;top:995px;width:546px;height:307px;background:linear-gradient(180deg,#d6dadc,#b7bcbd 60%,#6e7168);clip-path:polygon(0 0,490px 0,546px 56px,546px 100%,0 100%)" role="img" aria-label="Pastor in a black robe standing on a misty hilltop"></div>
<div class="photo" style="left:692px;top:995px;width:303px;height:307px;background:linear-gradient(135deg,#c9a24a,#e4e1d6 50%,#f1efea);clip-path:polygon(0 0,250px 0,303px 53px,303px 100%,0 100%)" role="img" aria-label="Nutritionist writing a meal plan beside a fruit basket"></div>
<div class="photo" style="left:1014px;top:995px;width:186px;height:307px;background:linear-gradient(135deg,#e7e3dc,#f2efe9 60%,#d9b98c)" role="img" aria-label="Dietitian at a desk with fresh fruit"></div>
<div class="abs heading" style="left:125px;top:1332px;font-size:19px;font-weight:800;color:var(--ink)">PASTOR</div>
<svg class="abs" style="left:571px;top:1317px" width="100" height="50" viewBox="0 0 100 50">
  <polygon points="22,1 43,12 43,38 22,49 1,38 1,12" fill="var(--gold)"/>
  <path d="M25 17l-8 8 8 8" stroke="var(--forest)" stroke-width="4" fill="none"/>
  <polygon points="78,1 99,12 99,38 78,49 57,38 57,12" fill="var(--gold)"/>
  <path d="M75 17l8 8-8 8" stroke="var(--forest)" stroke-width="4" fill="none"/>
</svg>

<!-- Breaking barriers -->
<div class="abs cream" style="left:34px;top:1476px;width:1132px;height:704px"></div>
<h2 class="abs" style="left:0;width:1200px;top:1568px;text-align:center;font-size:35px;line-height:44px">WHY CAMP 3874 IS BREAKING<br>BARRIERS</h2>
<p class="abs para" style="left:276px;width:648px;top:1668px;text-align:center">Geographical challenges make some communities difficult for missionaries to reach. The Camp 3874 program is designed to remove the physical limitations that can hinder us from bringing the Gospel to places that seem physically impossible to reach. Camp 3874 is founded on Romans 15:20. In his letter to the Romans, Paul requests funding to take the Gospel to Spain.</p>
<div class="abs" style="left:207px;top:1790px;width:788px;height:210px;border:2px solid var(--olive)"></div>
<div class="abs" style="left:207px;width:788px;top:1832px;text-align:center;font-size:17px;font-weight:600;color:var(--ink)">In this letter, he writes:</div>
<p class="abs" style="left:270px;width:662px;top:1870px;text-align:center;font-size:11px;line-height:17px;font-style:italic">“[20] and thus I make it my ambition to preach the gospel, not where Christ has already been named, lest I build on someone else’s foundation, [21] but it is written, “those who have never been told of him will see, and those who have never heard will understand.”</p>
<div class="abs" style="left:207px;width:788px;top:1938px;text-align:center;font-size:12px;font-weight:600;color:var(--ink)">Romans 15:20-21</div>
<div class="btn btn-gold" style="left:506px;top:2034px;width:188px;height:44px">Join Our Mission</div>

<!-- Training approach -->
<h2 class="section-title" style="top:2271px">CAMP 3874 MISSIONARY TRAINING<br>APPROACH</h2>
<div class="tab is-active" style="left:125px">Mind</div>
<div class="tab" style="left:366px">Body</div>
<div class="tab" style="left:610px">Spirit</div>
<div class="photo" style="left:125px;top:2502px;width:464px;height:464px;background:linear-gradient(135deg,#4d6fb8,#c99a7a 45%,#eceae6 75%,#9a9a96)" role="img" aria-label="Two women meditating with eyes closed in a gym"></div>
<svg class="abs" style="left:383px;top:2751px" width="234" height="263" viewBox="0 0 234 263" role="img" aria-label="Illustration of a brain lifting a barbell">
  <polygon points="70,4 164,4 230,70 230,193 164,259 70,259 4,193 4,70" fill="#f6e3d6" stroke="var(--gold)" stroke-width="8"/>
</svg>
<h3 class="abs" style="left:644px;top:2530px;font-size:32px;font-weight:800">MIND</h3>
<p class="abs" style="left:644px;width:340px;top:2580px;font-size:16px;line-height:23px">Psychologically, we will prepare the mind through counseling, breathing techniques, and simulations in order to prepare for psychological challenges that come with being in the field.</p>
<div class="btn btn-olive" style="left:644px;top:2716px;width:270px;height:44px">View our detailed training program</div>

<!-- Who is it for -->
<div class="abs cream" style="left:23px;top:3107px;width:1131px;height:810px"></div>
<h2 class="section-title" style="top:3194px">WHO IS CAMP 3874 FOR?</h2>
<div class="btn btn-outline" style="left:803px;top:3194px;width:272px;height:44px">View our Training Options</div>
<div class="photo" style="left:125px;top:3278px;width:302px;height:265px;background:linear-gradient(180deg,#9bb061,#c9d39d 50%,#6b7e8a)" role="img" aria-label="Woman meditating by a lake under trees"></div>
<div class="photo" style="left:449px;top:3278px;width:302px;height:265px;background:linear-gradient(135deg,#3f4f24,#8a9a4a 50%,#2e3a1c)" role="img" aria-label="Hands pressed together in prayer against greenery"></div>
<div class="photo" style="left:772px;top:3278px;width:303px;height:265px;background:linear-gradient(135deg,#a8b2bd,#5d7592 50%,#3d4a5c)" role="img" aria-label="Young man in a plaid shirt looking upward by a window"></div>
<div class="card-title" style="left:125px">ENDING AGENCIES FOR MISSIONARIES</div>
<p class="card-copy" style="left:125px;top:3652px">Are you looking to improve the training you’re offering your flock? We have designed a program to align our training with your goals to spread the Gospel to people and places where Jesus remains unnamed &amp; unknown. Our training helps turn your missionaries to resilient, well-trained men and women.</p>
<div class="card-title" style="left:449px">MISSIONARIES</div>
<p class="card-copy" style="left:449px;top:3627px">Are you independently seeking to develop your knowledge and skills independently? We are here to help! We can customize a training approach that fits your specific needs. Let us support your missionary journey to spread the Gospel to the most remote and treacherous areas in the world.</p>
<div class="card-title" style="left:772px">CHRISTIAN-BASED TRAINING PROGRAM FOR ALL!</div>
<p class="card-copy" style="left:772px;top:3677px">Are you looking to support the missionary community? Well we have a solution for you! We also offer a customized, personal-training approach for everyone. Even if you’re not preparing for a mission, joining one of our training programs will allow you to support our missionaries through your own physical fitness journey.</p>

<!-- Newsletter -->
<div class="abs" style="left:23px;top:3947px;width:1131px;height:347px;background:var(--mist)"></div>
<h2 class="section-title" style="top:4016px">JOIN OUR MISSIONARY<br>TRAINING:</h2>
<p class="abs" style="left:125px;width:490px;top:4110px;font-size:24px;line-height:33px">Stay up-to-date on our training programs, missionary success stories, and new program info!</p>
<div class="abs cream" style="left:673px;top:3989px;width:402px;height:246px"></div>
<p class="abs" style="left:705px;width:338px;top:4018px;text-align:center;font-size:12px;line-height:18px">Subscribe and help us in supporting our missionaries as they spread the Gospel to all corners and areas of the world</p>
<div class="abs" style="left:702px;top:4089px;width:347px;height:42px;border:1px solid var(--gold);background:var(--white);display:flex;align-items:center;justify-content:center;font-size:12px">Email Address</div>
<div class="btn btn-olive" style="left:776px;top:4156px;width:196px;height:44px">Subscribe</div>

<!-- Footer -->
<div class="abs footer"></div>
<svg class="abs" style="left:571px;top:4357px" width="58" height="71" viewBox="0 0 58 71">
  <polygon points="29,1 57,17 57,54 29,70 1,54 1,17" fill="var(--gold)"/>
  <path d="M29 52V20M21 28l8-8 8 8" stroke="var(--forest)" stroke-width="2.5" fill="none"/>
</svg>
<div class="abs" style="left:125px;top:4584px">
  <div style="font-family:'Montserrat',sans-serif;font-weight:900;font-size:40px;line-height:44px;color:var(--white)">CAMP 3874</div>
  <div style="font-family:'Montserrat',sans-serif;font-weight:700;font-size:11px;letter-spacing:4px;color:var(--white)">MIND + BODY + SPIRIT</div>
</div>
<div class="social" style="left:125px"></div>
<div class="social" style="left:167px"></div>
<div class="social" style="left:209px"></div>
<div class="social" style="left:251px"></div>
<div class="social" style="left:293px"></div>
<div class="social" style="left:335px"></div>
<div class="foot-head" style="left:477px">QUICK LINKS</div>
<div class="foot-link" style="top:4553px">Programs</div>
<div class="foot-link" style="top:4603px">Events</div>
<div class="foot-link" style="top:4654px">Online Store</div>
<div class="foot-link" style="top:4704px">About Us</div>
<div class="foot-link" style="top:4756px">Contact Us</div>
<div class="foot-head" style="left:771px">CONTACT INFO</div>
<div class="contact" style="top:4555px">
  <span class="contact-icon"><svg width="20" height="24" viewBox="0 0 20 24"><path d="M10 1a8 8 0 0 0-8 8c0 6 8 14 8 14s8-8 8-14a8 8 0 0 0-8-8z" fill="var(--forest)"/><circle cx="10" cy="9" r="3" fill="var(--gold)"/></svg></span>
  <span>trellis40, llc 410 harrow field ste b9<br>meridale la 70911</span>
</div>
<div class="contact" style="top:4637px">
  <span class="contact-icon"><svg width="22" height="22" viewBox="0 0 24 24"><path d="M6 2l4 4-2 3c1 3 4 6 7 7l3-2 4 4-3 4C10 22 2 14 2 5z" fill="var(--forest)"/></svg></span>
  <span>(555) 014-2283</span>
</div>
<div class="contact" style="top:4719px">
  <span class="contact-icon"><svg width="22" height="22" viewBox="0 0 24 24"><path d="M2 11L22 2l-6 20-4-8z" fill="var(--forest)"/></svg></span>
  <span>info@camp3874.example</span>
</div>

<div class="legal" style="left:125px">© Copyright © 2023 Trellis 40 All rights reserved.</div>
<div class="legal" style="left:740px;width:335px;text-align:right">Policies &nbsp;&nbsp;|&nbsp;&nbsp; Privacy policy &nbsp;&nbsp;|&nbsp;&nbsp; Terms &amp; Conditions</div>

</body>
</html>
```